Painting Company Business Card

Brightwell Painting needs a new business card. See attachments for our logo and current card as an example.
We want to utilize the same colors in the logo, and keep all the information that is currently on it. Just need an updated and modern design.
We are open to loosing the Association Logos if it means a better design.
We are also entertaining a spot for a picture of a headshot of the person listed on the card. Head shot can be finished later.

```html
<!DOCTYPE html>
<html lang="en">
<head>
<meta charset="utf-8">
<title>Brightwell Painting – Business Card</title>
<link rel="stylesheet" href="https://fonts.googleapis.com/css2?family=Open+Sans:wght@400;600;700&display=swap">
<style>
  :root {
    --backdrop: #c8cdd0;
    --card: #ffffff;
    --olive: #3b4030;
    --maroon: #6b2b2d;
    --ink: #2e2e2e;
  }
  * { margin: 0; padding: 0; box-sizing: border-box; }
  html, body { width: 1200px; height: 1200px; overflow: hidden; }
  body {
    background: var(--backdrop);
    font-family: "Open Sans", Arial, sans-serif;
    color: var(--ink);
    position: relative;
  }
  .card {
    position: absolute;
    left: 250px;
    width: 700px;
    height: 400px;
    background: var(--card);
  }
  .card--front { top: 146px; }
  .card--back { top: 652px; }

  .brand {
    position: absolute;
    display: flex;
    align-items: center;
    color: var(--olive);
    font-weight: 700;
  }
  .brand__name { line-height: 1.05; }
  .brand__mark { background: var(--maroon); flex: none; }

  .card--front .brand { left: 0; right: 0; top: 140px; justify-content: center; gap: 22px; }
  .card--front .brand__name { font-size: 54px; }
  .card--front .brand__mark { width: 26px; height: 26px; }

  .card--back .brand { left: 62px; top: 166px; gap: 10px; }
  .card--back .brand__name { font-size: 27px; }
  .card--back .brand__mark { width: 13px; height: 13px; }

  .divider {
    position: absolute;
    left: 293px; top: 88px;
    width: 3px; height: 232px;
    background: var(--olive);
  }
  .person { position: absolute; left: 343px; top: 84px; font-size: 20px; line-height: 23px; }
  .contact { position: absolute; left: 315px; list-style: none; font-size: 20px; display: flex; align-items: center; }
  .contact svg { width: 18px; height: 18px; margin-right: 10px; flex: none; }
  .contact--phone { top: 148px; }
  .contact--email { top: 187px; }
  .contact--web { top: 226px; }
  .services {
    position: absolute; left: 346px; top: 270px;
    display: grid; grid-template-columns: 164px auto; row-gap: 7px;
    font-size: 20px; list-style: none;
  }
</style>
</head>
<body>
  <section class="card card--front">
    <div class="brand">
      <span class="brand__name">Brightwell<br>Painting</span>
      <span class="brand__mark"></span>
    </div>
  </section>

  <section class="card card--back">
    <div class="brand">
      <span class="brand__name">Brightwell<br>Painting</span>
      <span class="brand__mark"></span>
    </div>
    <div class="divider"></div>
    <p class="person">Daniel Hayes<br>Manager</p>
    <div class="contact contact--phone">
      <svg viewBox="0 0 24 24"><path fill="#2e2e2e" d="M6.6 10.8a15 15 0 0 0 6.6 6.6l2.2-2.2a1 1 0 0 1 1-.25 11.4 11.4 0 0 0 3.6.57 1 1 0 0 1 1 1V20a1 1 0 0 1-1 1A17 17 0 0 1 3 4a1 1 0 0 1 1-1h3.5a1 1 0 0 1 1 1c0 1.25.2 2.45.57 3.57a1 1 0 0 1-.25 1z"/></svg>
      <span>555-014-2290</span>
    </div>
    <div class="contact contact--email">
      <svg viewBox="0 0 24 24" fill="none" stroke="#2e2e2e" stroke-width="1.6"><rect x="2.5" y="5" width="19" height="14"/><path d="M2.5 5l9.5 8 9.5-8M2.5 19l7-7M21.5 19l-7-7"/></svg>
      <span>Daniel.Brightwell@mail.com</span>
    </div>
    <div class="contact contact--web">
      <svg viewBox="0 0 24 24" fill="none" stroke="#2e2e2e" stroke-width="1.4"><circle cx="12" cy="12" r="9"/><ellipse cx="12" cy="12" rx="4" ry="9"/><path d="M3 12h18M5 7.5h14M5 16.5h14"/></svg>
      <span>BrightwellPainting.com</span>
    </div>
    <ul class="services">
      <li>Exterior Painting</li><li>Interior Painting</li>
      <li>Carpentry</li><li>&nbsp;Drywall</li>
    </ul>
  </section>
</body>
</html>
```